Sang chez la Vauq‘

“Vauq’” is the informal nickname used inside the French police for the "Brigade Vauquelin de Paris", an elite homicide unit. The apostrophe reflects spoken language and internal slang. The title Sang chez la Vauq’ highlights the central irony of the novel: a murder committed inside the very place meant to investigate murders.
Summary
A woman’s body is found inside the offices of Paris’s elite homicide squad. As detectives investigate, they uncover buried cases, internal rivalries and institutional silence. The closer they get to the truth, the clearer it becomes: this crime was meant to stay hidden.
Keywords : Woman’s body, Police procedural, Murder inside the police, Elite homicide unit, Dark realism, 14 quai des Lanternes.
Size : 16 x 24 cm
Title : Sang chez la Vauq'
Author : Julien Marsac
Publisher : Editions Ombrelle (at the bottom of the page)

```html
<!DOCTYPE html>
<html lang="fr">
<head>
<meta charset="utf-8">
<title>Sang chez la Vauq’ — Julien Marsac</title>
<link rel="stylesheet" href="https://fonts.googleapis.com/css2?family=Anton&family=Archivo+Black&family=EB+Garamond:wght@500&display=swap">
<style>
  :root {
    --page: #ffffff;
    --night: #15181c;
    --author-tan: #dcc7a6;
    --title-white: #efefeb;
    --title-red: #e2231a;
    --tape-yellow: #e0b626;
    --tape-ink: #16130c;
  }
  * { margin: 0; padding: 0; box-sizing: border-box; }
  html, body {
    width: 1200px; height: 1200px; overflow: hidden;
    background: var(--page);
  }
  .book-cover {
    position: absolute;
    left: 208px; top: 12px;
    width: 784px; height: 1176px;
    overflow: hidden;
    background: var(--night);
  }
  .cover-artwork {
    position: absolute; inset: 0;
    background:
      /* dark vignette */
      radial-gradient(ellipse 75% 60% at 50% 55%, transparent 55%, rgba(8,9,11,.85) 100%),
      /* blood pool on the floor */
      radial-gradient(ellipse 20% 5% at 47% 84%, rgba(150,22,14,.85), rgba(90,14,10,.5) 50%, transparent 80%),
      /* warm floor reflections */
      radial-gradient(ellipse 35% 8% at 70% 90%, rgba(190,140,80,.35), transparent 75%),
      radial-gradient(ellipse 30% 10% at 62% 74%, rgba(190,120,60,.35), transparent 75%),
      /* body area, dark blue-grey cloth tones */
      radial-gradient(ellipse 34% 9% at 58% 78%, rgba(60,66,78,.9), transparent 80%),
      /* desk lamp glow */
      radial-gradient(ellipse 14% 8% at 83% 60%, rgba(240,190,110,.8), transparent 75%),
      radial-gradient(ellipse 10% 5% at 87% 45%, rgba(255,220,150,.7), transparent 75%),
      /* evidence board */
      radial-gradient(ellipse 24% 14% at 80% 52%, rgba(170,120,70,.55), transparent 80%),
      /* doorway haze */
      radial-gradient(ellipse 9% 18% at 47% 58%, rgba(150,165,175,.55), transparent 80%),
      /* wall sign panel */
      radial-gradient(ellipse 17% 16% at 30% 53%, rgba(190,195,198,.55), transparent 80%),
      /* window blinds light, left */
      radial-gradient(ellipse 8% 16% at 4% 52%, rgba(160,170,180,.35), transparent 80%),
      /* desk band */
      linear-gradient(180deg, transparent 0%, transparent 66%, rgba(70,55,40,.55) 69%, rgba(40,34,28,.6) 75%, transparent 78%),
      /* texture */
      repeating-linear-gradient(115deg, rgba(255,255,255,.02) 0 2px, transparent 2px 7px),
      linear-gradient(180deg, #1d2126 0%, #262b31 35%, #33363a 55%, #24272b 70%, #2a2d31 85%, #141618 100%);
  }
  .author-name {
    position: absolute; top: 30px; left: 0; width: 100%;
    text-align: center;
    font-family: "Anton", sans-serif;
    font-size: 70px; letter-spacing: 2px;
    color: var(--author-tan);
    line-height: 1;
  }
  .title-main {
    position: absolute; top: 112px; left: 0; width: 100%;
    text-align: center;
    padding-left: 30px;
    font-family: "Archivo Black", sans-serif;
    font-weight: 400;
    font-size: 170px; line-height: 1;
    color: var(--title-white);
    letter-spacing: -3px;
  }
  .title-second {
    position: absolute; top: 286px; left: 0; width: 100%;
    display: flex; justify-content: center; align-items: baseline;
    padding-left: 80px;
    line-height: 1;
  }
  .title-link {
    font-family: "Archivo Black", sans-serif;
    font-size: 44px; color: var(--title-white);
    margin-right: 14px;
    transform: translateY(-64px);
  }
  .title-accent {
    font-family: "Archivo Black", sans-serif;
    font-size: 145px; color: var(--title-red);
    letter-spacing: -3px;
  }
  .crime-tape {
    position: absolute; left: -10px; top: 706px;
    width: 804px; height: 90px;
    background: linear-gradient(180deg, #d6aa1e, var(--tape-yellow) 30%, #e8c43a 70%, #c99c18);
    transform: rotate(0.6deg);
    display: flex; align-items: center; justify-content: center;
    box-shadow: 0 6px 14px rgba(0,0,0,.55);
  }
  .crime-tape span {
    font-family: "Anton", sans-serif;
    font-size: 62px; color: var(--tape-ink);
    letter-spacing: 1px;
    line-height: 1;
  }
  .publisher {
    position: absolute; bottom: 30px; left: 0; width: 100%;
    text-align: center;
    font-family: "EB Garamond", serif;
    font-weight: 500;
    font-size: 32px; color: var(--title-white);
  }
</style>
</head>
<body>
  <div class="book-cover">
    <div class="cover-artwork" role="img" aria-label="Illustration sombre : bureau de police de nuit avec panneau mural de la brigade, deux silhouettes dans l'embrasure d'une porte, tableau d'enquête éclairé par une lampe, et corps d'une femme étendu au sol dans une flaque de sang"></div>
    <div class="author-name">JULIEN MARSAC</div>
    <h1 class="title-main">Sang</h1>
    <div class="title-second">
      <span class="title-link">chez la</span>
      <span class="title-accent">Vauq’</span>
    </div>
    <div class="crime-tape"><span>SCÈNE DE CRIME - POLICE</span></div>
    <div class="publisher">Éditions Ombrelle</div>
  </div>
</body>
</html>
```